Global Expert Network Firm needs business card design

We need business card design for a new company based in Seoul, South Korea called 'Corwell Insight Partners'. We recruit industry experts covering all countries and connect our client and recruited expert by phone, face-to-face meetings and etc. We are a global expert network firm that is focused on delivering high-quality experts to our clients throughout the world. Our clients include multinational corporations, global consulting firms, private equity firms, venture capital firms, asset management companies.
We have made new logo and please find attachment.(Please use new logo)
Target Market(s)
Global Consulting Firms, Investment Firms, Private Equity Firms, Venture Capital Firms.
Industry/Entity Type
Recruitment
Contact Information for Business Card
We need two Languages (English and Korean Version).
The front is Korean and the back is English version.
[The back] [English]
Company Name: Corwell Insight Partners, Inc.
CEO Name: Daniel Park
Address: #507, Hanbit Bldg, 82 Maebongsan-ro, Dobong-gu, Seoul, 01327, Korea
Tel. +82 2 718 4052
Fax. +82 2 864 1097
Mobile. +82 10 7264 8815
Email: daniel@corwellip.com
Web: www.corwellip.com
[The front] [Korean] => Described in same order as English version.
회사명: 코웰인사이트파트너스(주)
대표이사: 박도현
주소: 서울시 도봉구 매봉산로 82 한빛빌딩 507호
Tel. 02 718 4052
Fax. 02 864 1097
Mobile. 010 7264 8815
Web: www.corwellip.com
Look and feel
Each slider illustrates characteristics of the customer's brand and the style your logo design should communicate.

```html
<!DOCTYPE html>
<html lang="en">
<head>
<meta charset="utf-8">
<title>Corwell Insight Partners — Business Cards</title>
<link rel="stylesheet" href="https://fonts.googleapis.com/css2?family=Cinzel:wght@400&family=Noto+Serif:wght@400&family=Noto+Serif+KR:wght@400&display=swap">
<style>
  :root {
    --navy: #1c2456;
    --paper: #ffffff;
    --ground: #eceae6;
    --silver-light: #d9dbde;
    --silver-dark: #a7a9ad;
    --ink: #1c2456;
    --muted: #4b5070;
    --rule: #8a8fa6;
  }
  * { margin: 0; padding: 0; box-sizing: border-box; }
  html, body { width: 1200px; height: 1200px; overflow: hidden; background: var(--ground); }
  .canvas { position: relative; width: 1200px; height: 1200px; }
  .card {
    position: absolute; left: 170px; width: 860px; height: 490px;
    background: var(--paper); overflow: hidden;
    box-shadow: 0 6px 18px rgba(0,0,0,.12);
    color: var(--ink); font-family: "Noto Serif", Georgia, serif;
  }
  .card--korean { top: 75px; }
  .card--english { top: 635px; }
  .card__shape { position: absolute; inset: 0; }
  .company-mark {
    position: absolute; left: 600px; top: 150px; width: 240px;
    color: var(--paper); font-family: "Noto Serif", Georgia, serif;
    font-size: 28px; line-height: 40px; font-weight: 400; text-align: center;
  }
  .holder { position: absolute; left: 70px; top: 130px; }
  .holder__name { font-family: "Cinzel", Georgia, serif; font-size: 38px; letter-spacing: 2px; line-height: 1; }
  .card--korean .holder__name { font-family: "Noto Serif KR", serif; font-size: 40px; letter-spacing: 4px; }
  .holder__title { font-size: 15px; margin-top: 10px; color: var(--muted); }
  .card--korean .holder__title { font-family: "Noto Serif KR", serif; }
  .contact { position: absolute; left: 70px; top: 262px; font-size: 16px; }
  .card--korean .contact { font-family: "Noto Serif KR", "Noto Serif", serif; }
  .contact__company { font-size: 17px; padding-bottom: 8px; border-bottom: 1px solid var(--rule); width: 470px; }
  .contact__list { list-style: none; padding: 8px 0; border-bottom: 1px solid var(--rule); width: 470px; }
  .contact__item { display: flex; align-items: center; gap: 10px; line-height: 24px; }
  .contact__address { display: flex; gap: 10px; padding-top: 8px; line-height: 22px; width: 470px; }
  .icon { width: 16px; height: 16px; flex: none; }
  .icon--pin { margin-top: 3px; }
</style>
</head>
<body>
<main class="canvas">

  <section class="card card--korean">
    <svg class="card__shape" viewBox="0 0 860 490" aria-hidden="true">
      <circle cx="748" cy="70" r="374" fill="var(--silver-light)"/>
      <circle cx="754" cy="66" r="366" fill="var(--silver-dark)"/>
      <circle cx="760" cy="60" r="360" fill="var(--navy)"/>
    </svg>
    <div class="company-mark">Corwell Insight Partners</div>
    <div class="holder">
      <div class="holder__name">박도현</div>
      <div class="holder__title">대표이사</div>
    </div>
    <div class="contact">
      <div class="contact__company">코웰인사이트파트너스(주)</div>
      <ul class="contact__list">
        <li class="contact__item"><svg class="icon" viewBox="0 0 16 16"><circle cx="8" cy="8" r="8" fill="var(--navy)"/><path d="M5 5.5h6v5H5z" fill="none" stroke="#fff" stroke-width="1.2"/></svg>Tel. 02 718 4052</li>
        <li class="contact__item"><svg class="icon" viewBox="0 0 16 16"><circle cx="8" cy="8" r="8" fill="var(--navy)"/><rect x="5" y="5" width="6" height="6" fill="none" stroke="#fff" stroke-width="1.2"/></svg>Fax. 02 864 1097</li>
        <li class="contact__item"><svg class="icon" viewBox="0 0 16 16"><circle cx="8" cy="8" r="8" fill="var(--navy)"/><rect x="6" y="4" width="4" height="8" rx="1" fill="none" stroke="#fff" stroke-width="1.2"/></svg>Mobile. 010 7264 8815</li>
        <li class="contact__item"><svg class="icon" viewBox="0 0 16 16"><circle cx="8" cy="8" r="8" fill="var(--navy)"/><circle cx="8" cy="8" r="3.5" fill="none" stroke="#fff" stroke-width="1.2"/></svg>www.corwellip.com</li>
        <li class="contact__item"><svg class="icon" viewBox="0 0 16 16"><circle cx="8" cy="8" r="8" fill="var(--navy)"/><path d="M4.5 5.5h7v5h-7zM4.5 5.5l3.5 3 3.5-3" fill="none" stroke="#fff" stroke-width="1.1"/></svg>daniel@corwellip.com</li>
      </ul>
      <div class="contact__address"><svg class="icon icon--pin" viewBox="0 0 16 16"><circle cx="8" cy="8" r="8" fill="var(--navy)"/><circle cx="8" cy="7" r="2.2" fill="#fff"/></svg><span>서울시 도봉구 매봉산로 82 한빛빌딩 507호</span></div>
    </div>
  </section>

  <section class="card card--english">
    <svg class="card__shape" viewBox="0 0 860 490" aria-hidden="true">
      <circle cx="748" cy="70" r="374" fill="var(--silver-light)"/>
      <circle cx="754" cy="66" r="366" fill="var(--silver-dark)"/>
      <circle cx="760" cy="60" r="360" fill="var(--navy)"/>
    </svg>
    <div class="company-mark">Corwell Insight Partners</div>
    <div class="holder">
      <div class="holder__name">DANIEL PARK</div>
      <div class="holder__title">CEO</div>
    </div>
    <div class="contact">
      <div class="contact__company">Corwell Insight Partners, Inc.</div>
      <ul class="contact__list">
        <li class="contact__item"><svg class="icon" viewBox="0 0 16 16"><circle cx="8" cy="8" r="8" fill="var(--navy)"/><path d="M5 5.5h6v5H5z" fill="none" stroke="#fff" stroke-width="1.2"/></svg>+82 2 718 4052</li>
        <li class="contact__item"><svg class="icon" viewBox="0 0 16 16"><circle cx="8" cy="8" r="8" fill="var(--navy)"/><rect x="5" y="5" width="6" height="6" fill="none" stroke="#fff" stroke-width="1.2"/></svg>+82 2 864 1097</li>
        <li class="contact__item"><svg class="icon" viewBox="0 0 16 16"><circle cx="8" cy="8" r="8" fill="var(--navy)"/><rect x="6" y="4" width="4" height="8" rx="1" fill="none" stroke="#fff" stroke-width="1.2"/></svg>+82 10 7264 8815</li>
        <li class="contact__item"><svg class="icon" viewBox="0 0 16 16"><circle cx="8" cy="8" r="8" fill="var(--navy)"/><circle cx="8" cy="8" r="3.5" fill="none" stroke="#fff" stroke-width="1.2"/></svg>www.corwellip.com</li>
        <li class="contact__item"><svg class="icon" viewBox="0 0 16 16"><circle cx="8" cy="8" r="8" fill="var(--navy)"/><path d="M4.5 5.5h7v5h-7zM4.5 5.5l3.5 3 3.5-3" fill="none" stroke="#fff" stroke-width="1.1"/></svg>daniel@corwellip.com</li>
      </ul>
      <div class="contact__address"><svg class="icon icon--pin" viewBox="0 0 16 16"><circle cx="8" cy="8" r="8" fill="var(--navy)"/><circle cx="8" cy="7" r="2.2" fill="#fff"/></svg><span>#507, Hanbit Bldg, 82 Maebongsan-ro,<br>Dobong-gu, Seoul, 01327, Korea</span></div>
    </div>
  </section>

</main>
</body>
</html>
```